Business Card Design Project : Tidewell Press

In preparation for market launch, Whistler's Tidewell Press require the development of a business card. Tidewell Press is a Community online publishing web portal. We provide the the city of Whistler located in B.C. (Canada) business directories, News, Classified ads, News, Events and blogs etc.

The main focus of the brand is to help local businesses to corporate with their online advertisement and marketing. Meeting our clients face to face is a must (B2B).

Target Market(s)

The target market is B2B customers. Business Owners to Marketing, advertising Managers

Industry/Entity Type

Business

Requirements
Must have
• - The business card will be two sided.
the BACK side will have our logo which consist of (icon, url,slogan) submited. The logo will be middle and centred.

The FRONT side should have company details:

Company Legal Name: FERNDALE TIDEWELL PRESS

Owen Marsk
Director of Sales & Marketing

www.ferndaletidewell.biz
owen@ferndaletidewell.biz

Phone: 555 014 3826
#2817 - 562 E. Harlow Ave.
Vancouver, B.C. K7P2R4 Canada
Nice to have
• - For the "FRONT" side of our business card. You can separate or re-arrange with our logo components (icon, logo,slogan). It does not have to be together.

Also our company legal name is rather long so arrange or organize the name in a way to make it shorter. Your experience and creativity will have to come in play.
Should not have
• should not have other colors beside logo color and black text (2 colors). Also nothing Three dimensional

```html
<!DOCTYPE html>
<html lang="en">
<head>
<meta charset="utf-8">
<title>Tidewell Press – Business Card</title>
<link href="https://fonts.googleapis.com/css2?family=Source+Sans+3:wght@400;600;700&display=swap" rel="stylesheet">
<style>
  :root {
    --brand-blue: #1f7cc1;
    --ink: #111111;
    --paper: #ffffff;
    --backdrop: #4a2c17;
  }
  * { margin: 0; padding: 0; box-sizing: border-box; }
  html, body {
    width: 1200px; height: 412px; overflow: hidden;
    background: var(--backdrop);
    font-family: "Source Sans 3", "Myriad Pro", Arial, sans-serif;
  }
  .stage { position: relative; width: 1200px; height: 412px; }
  .card {
    position: absolute; top: 64px; width: 498px; height: 285px; overflow: hidden;
  }
  .card--front { left: 74px; background: var(--paper); }
  .card--back { left: 629px; background: var(--brand-blue); }
  .front-shape { position: absolute; inset: 0; width: 100%; height: 100%; }

  .brand-name {
    position: absolute; left: 0; width: 100%; text-align: center;
    font-weight: 700; font-size: 27px; letter-spacing: 0.3px;
    display: flex; align-items: center; justify-content: center; gap: 9px;
  }
  .brand-name__dot { width: 16px; height: 16px; border-radius: 50%; }
  .lockup { position: absolute; text-align: center; }
  .lockup__url { font-weight: 700; font-size: 17px; line-height: 20px; letter-spacing: -0.1px; }
  .lockup__slogan { font-size: 13.5px; line-height: 16px; margin-top: 2px; }

  .card--front .lockup { left: 14px; width: 238px; top: 150px; }
  .card--front .lockup__url { color: var(--ink); }
  .card--front .lockup__slogan { color: var(--brand-blue); }
  .card--front .brand-name { top: 100px; width: 266px; color: var(--brand-blue); }
  .card--front .brand-name__dot { background: var(--brand-blue); }

  .card--back .lockup { left: 0; width: 100%; top: 156px; color: var(--paper); }
  .card--back .brand-name { top: 104px; color: var(--paper); }
  .card--back .brand-name__dot { background: var(--paper); }

  .details { position: absolute; left: 305px; top: 54px; color: var(--paper); }
  .details__company { font-weight: 700; font-size: 11.5px; letter-spacing: 0.2px; }
  .details__name { font-weight: 700; font-size: 16.5px; margin-top: 22px; line-height: 20px; }
  .details__title { font-size: 12.5px; line-height: 16px; }
  .details__contact { margin-top: 14px; font-size: 12.5px; line-height: 18px; }
  .details__row { display: flex; align-items: center; gap: 5px; }
  .details__row svg { width: 10px; height: 10px; fill: var(--paper); }
  .details__address { margin-top: 16px; font-size: 12.5px; line-height: 18px; }
</style>
</head>
<body>
<div class="stage">
  <section class="card card--front">
    <svg class="front-shape" viewBox="0 0 525 300" preserveAspectRatio="none" aria-hidden="true">
      <path fill="var(--ink)" d="M288,0 C303,40 291,90 273,140 C259,190 260,250 263,300 L267,300 C265,245 265,190 279,142 C297,90 308,40 296,0 Z"/>
      <path fill="var(--brand-blue)" d="M300,0 C313,40 302,92 284,142 C271,190 271,245 273,300 L525,300 L525,0 Z"/>
    </svg>
    <div class="brand-name"><span class="brand-name__dot"></span>Tidewell Press</div>
    <div class="lockup">
      <p class="lockup__url">www.ferndaletidewell.biz</p>
      <p class="lockup__slogan">Your information gateway</p>
    </div>
    <div class="details">
      <p class="details__company">FERNDALE TIDEWELL PRESS</p>
      <p class="details__name">Owen Marsk</p>
      <p class="details__title">Director of Sales &amp; Marketing</p>
      <div class="details__contact">
        <p class="details__row"><svg viewBox="0 0 10 10"><path d="M2 0.5 L3.6 2.6 L2.7 3.6 C3.3 5 4.9 6.6 6.4 7.3 L7.4 6.4 L9.5 8 L8.3 9.5 C4.5 9 1 5.5 0.5 1.7 Z"/></svg>555 014 3826</p>
        <p class="details__row"><svg viewBox="0 0 10 10"><path d="M0.5 2 H9.5 V8.5 H0.5 Z M1.2 2.6 L5 5.4 L8.8 2.6 Z" fill-rule="evenodd"/></svg>owen@ferndaletidewell.biz</p>
      </div>
      <div class="details__address">
        <p>#2817 - 562 E. Harlow Ave.</p>
        <p>Vancouver, B.C. K7P2R4 Canada</p>
      </div>
    </div>
  </section>

  <section class="card card--back">
    <div class="brand-name"><span class="brand-name__dot"></span>Tidewell Press</div>
    <div class="lockup">
      <p class="lockup__url">www.ferndaletidewell.biz</p>
      <p class="lockup__slogan">Your information gateway</p>
    </div>
  </section>
</div>
</body>
</html>
```